Harrowmere Fields Green Initiative Infographic

We need a flyer to distribute to new and existing tenants in our office park which explains our Green Initiatives. Harrowmere Fields Office Park is a Class A office park consisting of 5 commercial buildings and about 100 tenants. Some of our clients include Quillbyte, Vantorell and Dunmore Bask.

Please visit www.harrowmerefieldsofficepark.example for questions on our current "brand" and amenities. It is very important to follow the current “feel” we have on the website.

Here are the Green Initiatives we need to convey in this flyer:
1. All buildings Power Crest rated in 2009
2. Lighting and Energy Initiatives:
a.) Motion sensors added to all electrical and janitorial closest, storage areas and executive parking garages b.) Relamp from a 32W to a 28W bulb for all 2x4 fixtures in tenant offices and building common areas c.) Stairways relamped to 25W
d.) Relamped from T12 to T8 and LEDS in elevator cabs
e.) Relamped to LEDs in Elevators Lobby
f.) Relamped Restrooms to Compact Fluorescent

3. Plumbing: installed aerators on restroom faucets at .5 gallon per minute

4. Heating Ventilation Air Conditioning (HVAC) Energy Management System programming engineered for best performance. Secondly, all rooftop units have VFDs (Variable Frequency Drives) which controls fan speed for optimal efficiency.

5. Irrigation Systems all have rain sensors

6. Comprehensive recycling program includes the recycling of plastic, glass, cans, all types of paper, and cardboard. Secondly, construction recycling is required and captures about 70% for recycling

7. Implemented green contracts with janitorial, window cleaning, and pest control.

8. Sustainable purchasing procedures include items such as green cleaning products for janitorial and window cleaning

9. Annual Building Events such as a Page Trade where tenants donate used books in exchange for another book and the Transit Expo which partners with community partners: 781 Rideshare Services and the RVB Urban Rail Network.

10. 2013 earth day celebration will include a green fair, recycling awareness, education, commuting options, and several educational awareness events

Reason: Please submit designs as inforgraphics. Thank you.

• Must have:
"Harrowmere Fields Office Park" as prominent, same feel as website listed above, include all 10 initiaves,

```html
<!DOCTYPE html>
<html lang="en">
<head>
<meta charset="utf-8">
<title>Harrowmere Fields Office Park – Green Initiatives</title>
<link rel="stylesheet" href="https://fonts.googleapis.com/css2?family=Marcellus+SC&family=Roboto+Condensed:wght@300;400&display=swap">
<style>
  :root {
    --page: #ffffff;
    --sheet-light: #e3ead0;
    --sheet-mid: #d3dcb2;
    --band-dark: #8b9753;
    --band-deep: #7f8b48;
    --band-soft: #c9d4a3;
    --header-light: #e9eedb;
    --title: #6f7646;
    --brand: #4b4f33;
    --text-light: #ffffff;
    --seam: #eef2e1;
  }
  * { margin: 0; padding: 0; box-sizing: border-box; }
  html, body { width: 1200px; height: 951px; overflow: hidden; background: var(--page); }
  .canvas { position: relative; width: 1200px; height: 951px; background: var(--page);
    font-family: "Roboto Condensed", "Arial Narrow", sans-serif; color: var(--text-light); }

  .sheet { position: absolute; left: 49px; top: 49px; width: 1106px; height: 855px;
    background: linear-gradient(160deg, var(--sheet-light), var(--sheet-mid) 55%, var(--sheet-light)); }
  .column { position: absolute; top: 49px; height: 855px; }
  .column--left  { left: 49px;  width: 370px; background: linear-gradient(180deg, #dfe7c6, #d1dbaa); }
  .column--mid   { left: 421px; width: 367px; background: linear-gradient(180deg, #d6dfb6, #cfd9a9); }
  .column--right { left: 790px; width: 365px; background: linear-gradient(180deg, #dde5c2, #d3dcae); }
  .seam { position: absolute; top: 49px; width: 2px; height: 855px; background: var(--seam); }

  .masthead { position: absolute; left: 49px; top: 49px; width: 370px; height: 84px; background: var(--header-light); }
  .brand-mark { position: absolute; left: 67px; top: 71px; width: 44px; height: 44px; border-radius: 50%; background: var(--brand); }
  .brand-name { position: absolute; left: 139px; top: 76px; font-family: "Marcellus SC", serif;
    font-size: 23px; letter-spacing: 1px; color: var(--brand); white-space: nowrap; }
  .brand-sub { position: absolute; left: 139px; width: 256px; top: 100px; text-align: right;
    font-family: "Marcellus SC", serif; font-size: 13px; letter-spacing: 1.5px; color: var(--brand); }
  .title { position: absolute; left: 98px; top: 178px; font-size: 36px; font-weight: 400;
    color: var(--title); letter-spacing: 0.5px; }

  .band { position: absolute; font-size: 15px; line-height: 19px; font-weight: 400; }
  .fade-right { background: linear-gradient(90deg, var(--band-dark) 0%, var(--band-dark) 55%, rgba(139,151,83,0) 100%); }
  .fade-left  { background: linear-gradient(90deg, rgba(139,151,83,0) 0%, var(--band-dark) 45%, var(--band-dark) 100%); }
  .solid      { background: linear-gradient(90deg, #a4ae6c, var(--band-deep)); }

  .item-1  { left: 49px; top: 276px; width: 370px; height: 45px; padding: 13px 0 0 16px; }
  .item-2  { left: 49px; top: 381px; width: 370px; height: 45px; padding: 12px 16px 0 0; text-align: right; }
  .item-2-list { left: 49px; top: 426px; width: 370px; height: 248px; padding: 10px 24px 0 37px;
    font-size: 13.5px; line-height: 18px; background: linear-gradient(90deg, var(--band-soft), #bfcb92 60%, rgba(191,203,146,0.2)); }
  .item-3  { left: 49px; top: 677px; width: 370px; height: 62px; padding: 11px 20px 0 13px; }
  .item-4  { left: 421px; top: 126px; width: 367px; height: 149px; padding: 11px 20px 0 10px; }
  .item-5  { left: 421px; top: 324px; width: 367px; height: 53px; padding: 17px 0 0 57px; }
  .item-6  { left: 421px; top: 426px; width: 367px; height: 248px; padding: 69px 18px 0 16px; }
  .item-7  { left: 421px; top: 742px; width: 367px; height: 91px; padding: 14px 30px 0 77px; }
  .item-8  { left: 790px; top: 241px; width: 365px; height: 83px; padding: 11px 14px 0 16px; }
  .item-9  { left: 790px; top: 379px; width: 365px; height: 169px; padding: 15px 14px 0 64px; }
  .item-10 { left: 790px; top: 677px; width: 365px; height: 94px; padding: 11px 14px 0 16px; }
  .list-line { display: block; }
</style>
</head>
<body>
<main class="canvas">
  <div class="sheet"></div>
  <div class="column column--left"></div>
  <div class="column column--mid"></div>
  <div class="column column--right"></div>
  <div class="seam" style="left:419px"></div>
  <div class="seam" style="left:788px"></div>

  <header class="masthead"></header>
  <div class="brand-mark" aria-hidden="true"></div>
  <div class="brand-name">Harrowmere Fields</div>
  <div class="brand-sub">Office Park</div>
  <h1 class="title">Green Initiatives</h1>

  <p class="band fade-right item-1">1. All buildings Power Crest rated in 2009</p>
  <p class="band fade-left item-2">2. Lighting and Energy Initiatives:</p>
  <p class="band item-2-list">
    <span class="list-line">a.) Motion sensors added to all electrical and janitorial closest, storage areas and executive parking garages</span>
    <span class="list-line">b.) Relamp from a 32W to a 28W bulb for all 2x4 fixtures in tenant offices and building common areas c.) Stairways relamped to 25W</span>
    <span class="list-line">d.) Relamped from T12 to T8 and LEDS in elevator cabs</span>
    <span class="list-line">e.) Relamped to LEDs in Elevators Lobby</span>
    <span class="list-line">f.) Relamped Restrooms to Compact Fluorescent</span>
  </p>
  <p class="band fade-right item-3">3. Plumbing: installed aerators on restroom faucets at .5 gallon per minute</p>

  <p class="band solid item-4">4. Heating Ventilation Air Conditioning (HVAC) Energy Management System programming engineered for best performance. Secondly, all rooftop units have VFDs (Variable Frequency Drives) which controls fan speed for optimal efficiency.</p>
  <p class="band fade-left item-5">5. Irrigation Systems all have rain sensors</p>
  <p class="band solid item-6">6. Comprehensive recycling program includes the recycling of plastic, glass, cans, all types of paper, and cardboard. Secondly, construction recycling is required and captures about 70% for recycling</p>
  <p class="band fade-left item-7">7. Implemented green contracts with janitorial, window cleaning, and pest control.</p>

  <p class="band fade-right item-8">8. Sustainable purchasing procedures include items such as green cleaning products for janitorial and window cleaning</p>
  <p class="band fade-left item-9">9. Annual Building Events such as a Page Trade where tenants donate used books in exchange for another book and the Transit Expo which partners with community partners: 781 Rideshare Services and the RVB Urban Rail Network.</p>
  <p class="band fade-right item-10">10. 2013 earth day celebration will include a green fair, recycling awareness, education, commuting options, and several educational awareness events</p>
</main>
</body>
</html>
```